UI/UX design for non-profit education/student success foundation website

Looking to work with a ui/ux designer that can provide an elegant, impactful and modern responsive design for a non-profit education/student success foundation website. The website will need to have a lot of visuals and elements with impactful statements. The responsive templates will later be parsed (this will be done by another developer) and converted to Concrete5 CMS templates. The organization likes bold colors with a modern sleek design. Typography is also key in titles and statements of interest. On-scroll visuals could be nice if it lends well to combining imagery and text. The site will need templates for a homepage, global sub-page, and contact page. Interchangeable block elements would be nice if we want to create other templates or change element positions.

Target Market(s)

Continued education and philanthropy individuals/organizations

Industry/Entity Type

Non-profit / college education

Coding

Coded - Design and coding required

Number of Pages Required

3 page

Font styles to use
Sans Serif
Script

Colors
0094D4
00A9DD
6FCCEA
C7EBF8
E9F6FB
59FF00
82FF00
B8FF75
E3FFCB
F4FFEA
FFC000
F8CF3A
FAE287
FDF2CF
FEFAEE
EE7325
F08F49
F5BC92
FAE3D3
FDF4ED
6B429C
8869AF
B7A5CE
E3DAEB
F3F0F8

Requirements
Must have
• Modern responsive design, impactful visual elements, available theme elements pre styled for things like forms, buttoms, tables...
Nice to have
• Onscroll vidual effects, heros with background video

```html
<!DOCTYPE html>
<html lang="en">
<head>
<meta charset="utf-8">
<title>Font Variations — The Alder Foundation</title>
<link rel="stylesheet" href="https://fonts.googleapis.com/css2?family=Anton&family=Barlow+Semi+Condensed:wght@600&family=Bebas+Neue&family=Comfortaa:wght@400&family=Great+Vibes&family=Kaushan+Script&family=Marcellus&family=Montserrat:wght@600;700&family=Nunito:wght@600;700&family=Outfit:wght@400;500;600;700&family=Yellowtail&display=swap">
<style>
  :root {
    --orange: #EE7325;
    --ink: #2b2b2b;
    --muted: #c8c8c8;
    --title-grey: #e4e4e4;
    --white: #ffffff;
    --paper: #ffffff;
    --nav-gold: #FFC000;
  }
  * { margin: 0; padding: 0; box-sizing: border-box; }
  html, body { width: 1200px; height: 1037px; overflow: hidden; background: var(--paper); }
  .board { position: relative; width: 1200px; height: 1037px; }

  .board-title {
    position: absolute; top: 12px; left: 0; width: 1200px; text-align: center;
    font-family: "Bebas Neue", sans-serif; font-size: 88px; letter-spacing: 4px;
    color: var(--title-grey); line-height: 1;
  }

  /* hero mockups */
  .hero { position: absolute; left: 0; width: 468px; height: 287px; overflow: hidden; color: var(--white); }
  .hero--one { top: 124px; height: 281px; }
  .hero--two { top: 428px; }
  .hero--three { top: 742px; }
  .hero-photo {
    position: absolute; inset: 0;
    background:
      radial-gradient(ellipse at 30% 55%, rgba(196,160,130,.55), transparent 55%),
      radial-gradient(ellipse at 75% 40%, rgba(120,90,80,.5), transparent 50%),
      linear-gradient(180deg, #6e6a64 0%, #4c4a48 45%, #2d2e33 100%);
  }
  .hero-photo::after { content: ""; position: absolute; inset: 0; background: rgba(0,0,0,.28); }

  .brand {
    position: absolute; left: 41px; top: 8px; display: flex; align-items: center; gap: 4px;
    font-family: "Outfit", sans-serif; font-weight: 600; font-size: 10px; line-height: 9px; color: var(--white);
  }
  .brand-dot { width: 18px; height: 18px; border-radius: 50%; background: var(--white); opacity: .9; }

  .nav { position: absolute; top: 13px; left: 0; width: 100%; font-family: "Montserrat", sans-serif; font-weight: 700; font-size: 5px; letter-spacing: .2px; }
  .nav span { position: absolute; white-space: nowrap; }
  .nav .is-active::after { content: ""; position: absolute; left: 0; right: 0; top: 9px; height: 1px; background: var(--nav-gold); }

  .play { position: absolute; left: 227px; top: 93px; width: 22px; height: 22px; }

  .hero-copy { position: absolute; left: 0; width: 100%; text-align: center; }
  .hero-title { position: absolute; left: 0; width: 100%; text-align: center; line-height: 1; }
  .hero--one .hero-title { top: 121px; font-family: "Outfit", sans-serif; font-weight: 700; font-size: 25px; }
  .hero--two .hero-title { top: 122px; font-family: "Kaushan Script", cursive; font-size: 27px; }
  .hero--three .hero-title { top: 122px; font-family: "Outfit", sans-serif; font-weight: 600; font-size: 27px; }
  .hero-copy { top: 149px; font-size: 16px; line-height: 17.5px; }
  .hero--one .hero-copy { font-family: "Outfit", sans-serif; font-weight: 700; }
  .hero--two .hero-copy { top: 150px; font-family: "Montserrat", sans-serif; font-weight: 600; font-size: 15px; }
  .hero--three .hero-copy { top: 150px; font-family: "Outfit", sans-serif; font-weight: 500; font-size: 15.5px; }

  /* type specimen columns */
  .section-label { position: absolute; font-family: "Outfit", sans-serif; font-weight: 600; font-size: 24px; color: var(--muted); line-height: 1; }
  .label-options { left: 520px; top: 157px; }
  .label-cursive { left: 888px; top: 165px; }

  .specimen { position: absolute; left: 520px; color: var(--ink); font-size: 17.5px; line-height: 21px; white-space: nowrap; }
  .spec-outfit { top: 220px; font-family: "Outfit", sans-serif; font-weight: 600; }
  .spec-nunito { top: 296px; font-family: "Nunito", sans-serif; font-weight: 700; }
  .spec-montserrat { top: 383px; font-family: "Montserrat", sans-serif; font-weight: 600; }
  .spec-montserrat-bold { top: 462px; font-family: "Montserrat", sans-serif; font-weight: 700; font-size: 17px; }
  .spec-nunito-semi { top: 540px; font-family: "Nunito", sans-serif; font-weight: 700; }
  .spec-condensed { top: 628px; left: 521px; font-family: "Barlow Semi Condensed", sans-serif; font-weight: 600; font-size: 19px; }
  .spec-caps { top: 749px; left: 521px; font-family: "Montserrat", sans-serif; font-weight: 600; font-size: 18.5px; }

  .script { position: absolute; left: 890px; color: var(--orange); line-height: 1; white-space: nowrap; }
  .script-kaushan { top: 213px; font-family: "Kaushan Script", cursive; font-size: 33px; }
  .script-yellowtail { top: 288px; font-family: "Yellowtail", cursive; font-size: 48px; }
  .script-vibes { top: 372px; font-family: "Great Vibes", cursive; font-size: 56px; }
  .script-comfortaa { top: 474px; font-family: "Comfortaa", sans-serif; font-size: 46px; }
  .script-anton { top: 555px; font-family: "Anton", sans-serif; font-size: 40px; }
  .script-marcellus { top: 636px; font-family: "Marcellus", serif; font-size: 45px; letter-spacing: 1px; }
</style>
</head>
<body>
<main class="board">
  <h1 class="board-title">Font Variations</h1>

  <section class="hero hero--one">
    <div class="hero-photo" role="img" aria-label="Photo of students studying together around a table"></div>
    <div class="brand"><span class="brand-dot"></span><span>THE ALDER<br>FOUNDATION</span></div>
    <nav class="nav">
      <span class="is-active" style="left:174px">SERVICES</span><span style="left:227px">ABOUT US</span><span style="left:281px">DONATE</span><span style="left:331px">EDUCATION</span><span style="left:390px">CONTACT</span>
    </nav>
    <svg class="play" viewBox="0 0 22 22"><circle cx="11" cy="11" r="11" fill="#EE7325"/><path d="M9 7.5 L14 11 L9 14.5 Z" fill="#fff"/></svg>
    <h2 class="hero-title">OUR VISION</h2>
    <p class="hero-copy">We are not giving up on educating<br>the world’s most childrens</p>
  </section>

  <section class="hero hero--two">
    <div class="hero-photo" role="img" aria-label="Photo of students studying together around a table"></div>
    <div class="brand"><span class="brand-dot"></span><span>THE ALDER<br>FOUNDATION</span></div>
    <nav class="nav">
      <span class="is-active" style="left:171px">SERVICES</span><span style="left:224px">ABOUT US</span><span style="left:278px">DONATE</span><span style="left:328px">EDUCATION</span><span style="left:387px">CONTACT</span>
    </nav>
    <svg class="play" style="left:225px" viewBox="0 0 22 22"><circle cx="11" cy="11" r="11" fill="#EE7325"/><path d="M9 7.5 L14 11 L9 14.5 Z" fill="#fff"/></svg>
    <h2 class="hero-title">Our Vision</h2>
    <p class="hero-copy">We are not giving up on educating<br>the world’s most childrens</p>
  </section>

  <section class="hero hero--three">
    <div class="hero-photo" role="img" aria-label="Photo of students studying together around a table"></div>
    <div class="brand" style="left:46px"><span class="brand-dot"></span><span>THE ALDER<br>FOUNDATION</span></div>
    <nav class="nav">
      <span class="is-active" style="left:178px">SERVICES</span><span style="left:231px">ABOUT US</span><span style="left:285px">DONATE</span><span style="left:335px">EDUCATION</span><span style="left:394px">CONTACT</span>
    </nav>
    <svg class="play" style="left:225px" viewBox="0 0 22 22"><circle cx="11" cy="11" r="11" fill="#EE7325"/><path d="M9 7.5 L14 11 L9 14.5 Z" fill="#fff"/></svg>
    <h2 class="hero-title">Our Vision</h2>
    <p class="hero-copy">We are not giving up on educating<br>the world’s most childrens</p>
  </section>

  <h3 class="section-label label-options">FONT OPTIONS</h3>
  <h3 class="section-label label-cursive">CURSIVE FONT</h3>

  <p class="specimen spec-outfit">We are not giving up on educating<br>the world’s most childrens</p>
  <p class="specimen spec-nunito">We are not giving up on educating<br>the world’s most childrens</p>
  <p class="specimen spec-montserrat">We are not giving up on educating<br>the world’s most childrens</p>
  <p class="specimen spec-montserrat-bold">We are not giving up on educating<br>the world’s most childrens</p>
  <p class="specimen spec-nunito-semi">We are not giving up on educating<br>the world’s most childrens</p>
  <p class="specimen spec-condensed">WE ARE NOT GIVING UP ON EDUCATING<br>THE WORLD’S MOST CHILDRENS</p>
  <p class="specimen spec-caps">WE ARE NOT GIVING UP ON EDUCATING<br>THE WORLD’S MOST CHILDRENS</p>

  <p class="script script-kaushan">Our Vision</p>
  <p class="script script-yellowtail">Our Vision</p>
  <p class="script script-vibes">Our Vision</p>
  <p class="script script-comfortaa">Our Vision</p>
  <p class="script script-anton">Our Vision</p>
  <p class="script script-marcellus">OUR VISION</p>
</main>
</body>
</html>
```